Documentary Film Poster Design Project

I'm looking to hire someone to design a 11 x 17 poster for my documentary film, "Past the Shoal," which is about plastic pollution in the atlantic ocean. The film is accepted into four film international film festivals (so far), so your design would have wide exposure.

www.pasttheshoal-film.example

I'm looking for something fairly straightforward, that incorporates some textual information for the film, along with (maybe) existing photographs and your amazing design skills. Please do not include images of PET soda/water bottles. The film has a science advisory board which is very specific about using the correct representation of oceanic plastic pollution.

I'd like to own the rights to this poster and have the poster be scalable to printed postcards and DVD packaging.

Target Market(s)

This poster will be used at film festivals to promote the film and attract viewers to attend. It should be bold and striking, making people take notice of it and say, "that's a cool poster, I'd like to see that film about plastic pollution. It also looks like it was filmed on a ship. cool."

Industry/Entity Type

Plastic

Requirements
Must have
• The poster must have the following textual information in it. Basically as you see in any movie poster. I'm looking for interesting typography in this poster, especially with the title. In someway, I think it would be nice to play with the idea of little pieces of plastic in the visual look of the title, but that's for you to decide. I've also attached images of the motion-graphics in the film, but do not feel like you have to use these.

Past the Shoal

A documentary about plastic pollution

A 812reels production A film by Mark Dunbury
cinematography by Mark Dunbury and Lou Tarnowitzky edited by Mark Dunbury written by Mark Dunbury and Nora Dunbury produced and directed by Mark Dunbury

www.pasttheshoal-film.example
www.facebook.com/PastTheShoalFilm

```html
<!DOCTYPE html>
<html lang="en">
<head>
<meta charset="utf-8">
<title>Past the Shoal — Poster</title>
<link rel="stylesheet" href="https://fonts.googleapis.com/css2?family=Anton&family=Oswald:wght@500;700&family=Roboto:wght@400&display=swap">
<style>
  :root {
    --page: #ffffff;
    --title: #cfe0f5;
    --ink: #ffffff;
    --credit: #e9e9e9;
    --night: #070707;
  }
  html, body {
    margin: 0;
    width: 1200px;
    height: 900px;
    overflow: hidden;
    background: var(--page);
  }
  .poster {
    position: absolute;
    left: 322px;
    top: 14px;
    width: 565px;
    height: 872px;
    overflow: hidden;
    background: var(--night);
  }
  .seascape {
    position: absolute;
    inset: 0;
    background:
      linear-gradient(to bottom, rgba(7,7,7,0) 0%, rgba(7,7,7,0) 74%, rgba(7,7,7,0.85) 88%, var(--night) 95%),
      linear-gradient(to right,
        #9c8a92 0%, #7b8595 6%, #46464f 14%, #5d6470 22%, #3b3a42 30%,
        #8b7b58 38%, #6a5a44 44%, #4a3d32 52%, #33291f 64%, #1d1815 80%, #0c0a0a 100%);
  }
  .title-block {
    position: absolute;
    left: 150px;
    top: 186px;
    width: 260px;
    text-align: center;
  }
  .title {
    margin: 0;
    font-family: "Anton", sans-serif;
    font-weight: 400;
    font-size: 124px;
    line-height: 0.86;
    color: var(--title);
    text-transform: lowercase;
    letter-spacing: 1px;
  }
  .title span { display: block; }
  .tagline {
    position: absolute;
    left: 110px;
    top: 524px;
    width: 340px;
    margin: 0;
    text-align: center;
    font-family: "Oswald", sans-serif;
    font-weight: 700;
    font-size: 13px;
    color: var(--ink);
    white-space: nowrap;
  }
  .tagline .plastic { color: var(--title); }
  .credits {
    position: absolute;
    left: 0;
    right: 0;
    top: 788px;
    text-align: center;
    font-family: "Oswald", sans-serif;
    font-weight: 500;
    color: var(--credit);
    text-transform: uppercase;
  }
  .credits p { margin: 0 0 2px; font-size: 11px; line-height: 1.1; letter-spacing: 0.2px; }
  .credits small { font-size: 5px; letter-spacing: 0.3px; margin: 0 2px; }
  .site {
    position: absolute;
    left: 0;
    right: 0;
    top: 855px;
    text-align: center;
    font-family: "Roboto", sans-serif;
    font-size: 8px;
    color: var(--credit);
  }
</style>
</head>
<body>
  <main class="poster">
    <div class="seascape" role="img" aria-label="Sideways photograph of a sunset sky with dark clouds meeting a dark rippling ocean"></div>

    <div class="title-block">
      <h1 class="title"><span>past</span><span>the</span><span>shoal</span></h1>
    </div>
    <p class="tagline">a documentary about <span class="plastic">plastic</span> pollution</p>

    <section class="credits">
      <p><small>a</small>812reels<small>production</small> <small>a film by</small>Mark Dunbury</p>
      <p><small>cinematography by</small>Mark Dunbury<small>and</small>Lou Tarnowitzky <small>edited by</small>Mark Dunbury</p>
      <p><small>written by</small>Mark Dunbury<small>and</small>Nora Dunbury <small>produced and directed by</small>Mark Dunbury</p>
    </section>
    <div class="site">www.pasttheshoal-film.example</div>
  </main>
</body>
</html>
```